Tandrew Advisory Group Business Card Design Project

2-sided business card for my small (me and a couple subcontractors) firm, which consults to public community colleges and school districts and public agencies in California on energy matters, mostly solar electric systems that can reduce their electricity use by as much as 80%. I prepare requests for proposals (RFPs), manage the RFP processes, and work with the solar vendors to get the best deal for my clients. I also do regulatory and legislative advocacy for strong renewable energy policies. I do lots of quantitative analysis to make sure the solar systems are sized to produce the maximum monetary savings and focus a lot on the aesthetic design of the solar systems, as architectural features of the campuses (most are carport structures built in parking lots, but some are built on the ground and on rooftops). All my work is geared to getting the best value, highest quality, and most reliable solar system. My career background is in public interest energy advocacy; I'm not a consultant trying to make a million dollars but someone who is still serving in the public interest.

My competition is made up of much larger firms; this business card/logo in large part is intended to present an image of my firm as an equal to these larger firms despite my smaller size.

Essential information as follows:
Firm name: Tandrew Advisory Group
Tagline: Clean Energy Procurement for the Public Sector
Name: Gavin Tandrew
email, 2 phone number, and address listed as well.

Target Market(s)

Public schools, community colleges, & public agencies.There is a wide range in the sophistication of these organizations.

Industry/Entity Type

Parking

Requirements
Must have
• - several rich colors, which can be either in the logo or in the background - the overall feeling of the card should reflect richness of color. I have uploaded some photos showing some colors that I like together. By rich I do not necessarily mean bright. I suppose bright colors in the logo could be supported with rich colors in the overall background of the card.
- professional, and powerful in an understated way (not kooky, cartoonish, or very playful)
- the logo must NOT be too representational of solar energy or the sun, but at the same time it would be good for the logo to be somewhat suggestive of this.

Nice to have
• -I like abstract and geometric images (with rich colts).
- A very subtle reference to schools/colleges/education would be great but it CANNOT be explicit; it would have to be faintly suggestive.
- In the logo I like the idea of abstract or geometric shapes intersecting with other in an interesting and suggestive way, conveying the multiple aspects of my practice (economics, data analysis, energy analysis, problem solving, managing collaborative processes, policy analysis)
- My work relates to environmental concerns, especially climate change. Working this into the logo in a subtle way could be good, but it's not a requirement.
- I like the idea that the logo/card feels serene.
- In designing the business card, I kind of like the idea of having the tag line as the first thing they read, then they see the firm name.

Should not have
• Not:
- humorous
- boring
- overly slick
- overly formal
- whimsical

```html
<!DOCTYPE html>
<html lang="en">
<head>
<meta charset="utf-8">
<title>Tandrew Advisory Group – Business Card</title>
<link rel="stylesheet" href="https://fonts.googleapis.com/css2?family=Quicksand:wght@400;500&family=Montserrat:wght@700&display=swap">
<style>
  :root {
    --page: #ffffff;
    --card-light: #6d6e70;
    --card-mid: #555658;
    --card-dark: #38393b;
    --sun: #fdc93f;
    --sky: #00adee;
    --ink-light: #ffffff;
  }
  * { margin: 0; padding: 0; box-sizing: border-box; }
  html, body { width: 1200px; height: 785px; overflow: hidden; background: var(--page); }
  .canvas { position: relative; width: 1200px; height: 785px; }

  .card {
    position: absolute;
    top: 49px;
    width: 374px;
    height: 647px;
    background: radial-gradient(ellipse at 25% 12%, var(--card-light) 0%, var(--card-mid) 45%, var(--card-dark) 100%);
    color: var(--ink-light);
    font-family: "Quicksand", sans-serif;
    overflow: hidden;
  }
  .card--front { left: 107px; }
  .card--back { left: 684px; }

  /* Brand name lockup */
  .brand { position: absolute; left: 0; right: 0; text-align: center; }
  .brand__square { display: block; margin: 0 auto; background: var(--sun); }
  .brand__name {
    font-family: "Quicksand", sans-serif;
    font-weight: 400;
    color: var(--ink-light);
    text-transform: uppercase;
    line-height: 1;
  }
  .brand__name-main, .brand__name-sub { display: block; }

  .card--front .brand { top: 158px; }
  .card--front .brand__square { width: 200px; height: 200px; margin-bottom: 16px; }
  .card--front .brand__name-main { font-size: 46px; letter-spacing: 0.02em; }
  .card--front .brand__name-sub { font-size: 18px; letter-spacing: 0.03em; margin-top: 4px; }

  .card--back .brand { top: 38px; }
  .card--back .brand__square { width: 136px; height: 136px; margin-bottom: 8px; }
  .card--back .brand__name-main { font-size: 32px; letter-spacing: 0.02em; }
  .card--back .brand__name-sub { font-size: 12.5px; letter-spacing: 0.03em; margin-top: 2px; }

  /* Front tagline band */
  .tagline {
    position: absolute;
    left: 0; right: 0;
    top: 566px;
    height: 59px;
    background: var(--sky);
    display: flex; align-items: center; justify-content: center;
    text-align: center;
    font-family: "Montserrat", sans-serif;
    font-weight: 700;
    font-size: 17px;
    line-height: 1.4;
    text-transform: uppercase;
    color: var(--ink-light);
  }

  /* Back details */
  .person {
    position: absolute; left: 0; right: 0; top: 328px;
    text-align: center;
    font-size: 38px; font-weight: 400; line-height: 1.2; letter-spacing: 0.01em;
  }
  .contacts {
    position: absolute; left: 80px; top: 405px;
    list-style: none;
  }
  .contact {
    display: flex; align-items: center;
    height: 28px; margin-bottom: 11px;
    font-size: 22px; font-weight: 400; white-space: nowrap;
  }
  .contact__icon { width: 28px; height: 28px; margin-right: 10px; flex: none; }
  .bottom-bar {
    position: absolute; left: 0; right: 0; bottom: 0;
    height: 17px; background: var(--sky);
  }
</style>
</head>
<body>
<main class="canvas">

  <section class="card card--front" aria-label="Card front">
    <div class="brand">
      <span class="brand__square"></span>
      <p class="brand__name"><span class="brand__name-main">Tandrew</span><span class="brand__name-sub">Advisory Group</span></p>
    </div>
    <p class="tagline">Clean Energy Procurement<br>for the Public Sector</p>
  </section>

  <section class="card card--back" aria-label="Card back">
    <div class="brand">
      <span class="brand__square"></span>
      <p class="brand__name"><span class="brand__name-main">Tandrew</span><span class="brand__name-sub">Advisory Group</span></p>
    </div>

    <h1 class="person">Gavin Tandrew</h1>

    <ul class="contacts">
      <li class="contact">
        <svg class="contact__icon" viewBox="0 0 29 29" aria-hidden="true">
          <rect width="29" height="29" rx="4" fill="#fdc93f"/>
          <rect x="9.5" y="5" width="10" height="19" rx="1.8" fill="none" stroke="#fff" stroke-width="2"/>
          <circle cx="14.5" cy="20.5" r="1.2" fill="#fff"/>
        </svg>
        <span>+1 916 555 0142</span>
      </li>
      <li class="contact">
        <svg class="contact__icon" viewBox="0 0 29 29" aria-hidden="true">
          <rect width="29" height="29" rx="4" fill="#fdc93f"/>
          <path d="M9 6.5c1-.6 2-.4 2.5.5l1.6 3c.4.8.2 1.6-.5 2.1l-1.2.9c.8 2 2.3 3.6 4.3 4.6l.9-1.2c.5-.7 1.4-.9 2.1-.5l3 1.6c.9.5 1.1 1.5.5 2.5l-1 1.5c-.7 1-2 1.4-3.2 1-5.2-1.8-9-5.6-10.8-10.8-.4-1.2 0-2.5 1-3.2z" fill="#fff"/>
        </svg>
        <span>916 555 0187</span>
      </li>
      <li class="contact">
        <svg class="contact__icon" viewBox="0 0 29 29" aria-hidden="true">
          <rect width="29" height="29" rx="4" fill="#fdc93f"/>
          <rect x="6" y="9" width="17" height="12" rx="1" fill="#fff"/>
          <path d="M6.5 9.5l8 6 8-6" fill="none" stroke="#fdc93f" stroke-width="1.6"/>
        </svg>
        <span>info@tandrew.com</span>
      </li>
    </ul>

    <div class="bottom-bar"></div>
  </section>

</main>
</body>
</html>
```